Zielgruppe
brinko handel ist eine Vertriebsagentur, die sich ausschließlich auf den BtoB Vertrieb spezialisiert hat. Wir agieren seit 19 Jahren am Markt und sind mehrfach ausgezeichneter Exzellenzberater des Mittelstandes. Wir unterstützen mittelständische Unternehmen, Familienunternehmen, Start up´s in der Wachstumsphase und Großkonzerne in der Industrie und im Dienstleistungsbereich. Ansprechpartner für uns sind Vertriebsleiter und GF´s in den Unternehmen.
Aufgabenstellung
Wir möchten unsere Angebotsvorlage neu im Layout neu designen lassen. Sie soll unsere Arbeitsweise zielgenau - authentisch - pfiffig widerspiegeln. Ich möchte gerne eine moderne und klare Struktur. Auf einer Seite sollen unsere USP´s dargestellt werden und auf ein - zwei Seiten ist das Angebot - in den folgenden Seiten sind die Vertragsinhalte.

```html
<!DOCTYPE html>
<html lang="de">
<head>
<meta charset="utf-8">
<title>Ihre Vorteile – Angebot</title>
<link href="https://fonts.googleapis.com/css2?family=Arimo:wght@400;700&display=swap" rel="stylesheet">
<style>
  :root{
    --bg:#dedede;
    --page:#f2f2f2;
    --blue:#234a8d;
    --accent:#e0634e;
    --rule:#d6d6d6;
    --card:#dcdcdc;
    --heading:#4a4a4a;
    --text:#3c3c3c;
    --icon:#2b2b2b;
  }
  *{box-sizing:border-box;margin:0;padding:0}
  html,body{width:1200px;height:1200px;overflow:hidden}
  body{background:var(--bg);font-family:"Arimo",Arial,sans-serif;color:var(--text)}
  .page{position:absolute;left:200px;top:36px;width:800px;height:1128px;background:var(--page);box-shadow:0 6px 22px rgba(0,0,0,.12)}
  .page-header{position:absolute;left:40px;right:40px;top:44px;display:flex;justify-content:space-between;align-items:baseline;font-size:11.5px;font-weight:700}
  .offer-no{color:var(--accent)}
  .page-no{color:var(--heading);font-size:9px}
  .header-rule{position:absolute;left:40px;right:40px;top:74px;height:4px;background:var(--rule)}
  .title{position:absolute;left:0;right:0;top:168px;text-align:center;font-size:40px;font-weight:700;color:var(--blue)}
  .title-rule{position:absolute;left:170px;width:460px;top:252px;height:3px;background:#555}
  .benefits{position:absolute;left:57px;top:339px;width:700px;display:grid;grid-template-columns:repeat(4,167px);grid-template-rows:322px 322px;column-gap:11px;row-gap:22px}
  .benefit{background:var(--card);text-align:center;padding:16px 10px 0}
  .benefit-icon{width:66px;height:66px;margin:0 auto;border:4px solid var(--blue);border-radius:50%;background:#f7f7f7;display:flex;align-items:center;justify-content:center}
  .benefit-icon svg{width:32px;height:32px;fill:none;stroke:var(--icon);stroke-width:1.6;stroke-linecap:round;stroke-linejoin:round}
  .benefit-title{height:54px;margin-top:18px;display:flex;align-items:center;justify-content:center;font-size:15.5px;font-weight:700;color:var(--heading);line-height:1.2;letter-spacing:.3px}
  .benefit-text{margin-top:6px;font-size:11.6px;line-height:1.38;color:var(--text)}
  .footer-rule{position:absolute;left:40px;right:40px;top:1070px;height:3px;background:var(--rule)}
  .page-footer{position:absolute;left:40px;right:40px;top:1086px;font-size:12px;color:#222;white-space:nowrap}
</style>
</head>
<body>
<main class="page">
  <header class="page-header">
    <span class="offer-no">Angebot-Nr. 20221008</span>
    <span class="page-no">3</span>
  </header>
  <div class="header-rule"></div>

  <h1 class="title">Ihre Vorteile</h1>
  <div class="title-rule"></div>

  <section class="benefits">
    <article class="benefit">
      <div class="benefit-icon"><svg viewBox="0 0 32 32"><path d="M9 5l4 5-2.5 2.5c1.5 3.5 4 6 8 8L21 18l5 4-2.5 3.5C16 25 7 16 6 8.5Z"/><path d="M19 6a8 8 0 0 1 7 7M19 10a4 4 0 0 1 3 3"/></svg></div>
      <h2 class="benefit-title">ENTSCHEIDER</h2>
      <p class="benefit-text">Wir führen 12.000 Gespräche im Monat mit Vorständen, Geschäfts­führern, Marketing-, Vertriebs- und Einkaufsleitern</p>
    </article>
    <article class="benefit">
      <div class="benefit-icon"><svg viewBox="0 0 32 32"><rect x="6" y="8" width="20" height="18" rx="2"/><path d="M6 13h20M11 5v5M21 5v5"/></svg></div>
      <h2 class="benefit-title">RICHTIGER<br>ZEITPUNKT</h2>
      <p class="benefit-text">Wir haben das Fingerspitz­engefühl beim Interessent­en zum richtigen Zeitpunkt der Entscheidung präsent zu sein, ohne penetrant zu wirken</p>
    </article>
    <article class="benefit">
      <div class="benefit-icon"><svg viewBox="0 0 32 32"><rect x="5" y="5" width="18" height="12"/><path d="M8 14l4-4 3 2 5-5"/><circle cx="14" cy="22" r="2.2"/><circle cx="23" cy="22" r="2.2"/><path d="M10 28c0-2 2-3 4-3s4 1 4 3M19 28c0-2 2-3 4-3s4 1 4 3"/></svg></div>
      <h2 class="benefit-title">VERTRIEBSAFFIN</h2>
      <p class="benefit-text">Kompetenz und vor allem Erfahrungen im Vertrieb lassen uns schnell und zielsicher für Sie agieren. Wir wissen wie wir die richtigen Ansprechpartner kontaktieren und auch begeistern können.</p>
    </article>
    <article class="benefit">
      <div class="benefit-icon"><svg viewBox="0 0 32 32"><rect x="6" y="6" width="20" height="20" rx="1"/><rect x="11" y="11" width="10" height="10"/><path d="M14 14h4v4h-4zM11 3v3M16 3v3M21 3v3M11 26v3M16 26v3M21 26v3M3 11h3M3 16h3M3 21h3M26 11h3M26 16h3M26 21h3"/></svg></div>
      <h2 class="benefit-title">TECHNIKKOM-<br>PETENZ</h2>
      <p class="benefit-text">Durch unser technisches Interesse und die Möglich­keit, die wichtigsten Faktoren in der Akquise für den Ansprechpartner zu identifizieren, können wir in komplexen technischen Projekten agieren.</p>
    </article>

    <article class="benefit">
      <div class="benefit-icon"><svg viewBox="0 0 32 32"><rect x="8" y="14" width="16" height="13" rx="1.5"/><path d="M11 14v-3a5 5 0 0 1 10 0v3M16 19v3"/></svg></div>
      <h2 class="benefit-title">VERTRAUEN</h2>
      <p class="benefit-text">Ihre Kundendaten sind bei uns in sicheren Händen. Wir arbeiten auf eigenen Servern die täglich 2-fach gesichert werden. Eine Verschwiegenheit­serklärung nach dem DGSVO ist für uns selbst­verständlich!</p>
    </article>
    <article class="benefit">
      <div class="benefit-icon"><svg viewBox="0 0 32 32"><circle cx="16" cy="14" r="3"/><path d="M10 20a8 8 0 1 1 12 0M7 23a12 12 0 1 1 18 0M12 27l4-10 4 10"/></svg></div>
      <h2 class="benefit-title">VOLLE<br>KONZENTRATION</h2>
      <p class="benefit-text">Unsere Mitarbeiter sind alle Muttersprachler, arbeiten in einzelnen Büros –kein Homeoffice- für eine ruhige Atmosphäre und optimale Konzentration. Unser Sitz ist in Deutschland.</p>
    </article>
    <article class="benefit">
      <div class="benefit-icon"><svg viewBox="0 0 32 32"><rect x="8" y="6" width="16" height="22" rx="1.5"/><rect x="12" y="4" width="8" height="4" rx="1"/><path d="M12 17l3 3 6-6"/></svg></div>
      <h2 class="benefit-title">QUALITÄT</h2>
      <p class="benefit-text">Unsere Team wird per­manent geschult durch Team- und Einzelcoach­ing. Es finden regelmäßig Projektbesprechungen statt. Dabei wird auch der Akquiseprozess belebt und das Gesprächskonzept flexibel angepasst.</p>
    </article>
    <article class="benefit">
      <div class="benefit-icon"><svg viewBox="0 0 32 32"><circle cx="16" cy="16" r="11"/><path d="M16 9v7h6"/></svg></div>
      <h2 class="benefit-title">NO LIMIT</h2>
      <p class="benefit-text">Unsere Gespräche sind nicht zeitlich begrenzt. Der Gesprächspartner bes­timmt den Zeitpunkt der erneuten Kontaktaufnahme und die Gesprächsdauer. Qualität vor Quantität ist unser Prinzip!</p>
    </article>
  </section>

  <div class="footer-rule"></div>
  <footer class="page-footer">Marlen Vossberg &nbsp;|&nbsp; +49 (0) 170 482 316 7 &nbsp;|&nbsp; mv@brinko-handel.de &nbsp;|&nbsp; Lindenweg 12 &nbsp;|&nbsp; 91054 Erlangen &nbsp;|&nbsp; 09131 604 218 0</footer>
</main>
</body>
</html>
```